依頼詳細
お客様にわかりやすく、またチラシをみてポイントカードを持っておきたい、もらっておきたいと思わせるデザインを希望します。お客様の目に入りやすく、A1のポスターや、レジ横でA4の用紙に置く予定です。
内容はジュース1杯で1P
10Pでお好きなドリンク1杯サービスです!(どのサイズでも)
入会費、年会費無料、有効期限なし!
記載項目
ポイントカード
サイズ
A4
ページ数
片面
希望イメージ
シンプル 複雑
単色 カラフル
暗い 明るい
日常 高級
遊び心 厳粛
未来的 伝統的
女性的 男性的
希望する色
黄・オレンジ系
納品ファイル
• 高解像度JPG (.jpg)
補足説明
参考イメージ添付します。
依頼公開後の追記内容
ポイントカード画像を添付します。
■ 選んだ理由

ポイントカードが目立つ

■ 提案者全員のお礼・コメント

どれもレベルが高い提案で選ぶことが難しかったです。また機会がございましたらよろしくお願いします。

```html
<!DOCTYPE html>
<html lang="ja">
<head>
<meta charset="utf-8">
<title>ポイントカードのご案内</title>
<link rel="stylesheet" href="https://fonts.googleapis.com/css2?family=M+PLUS+Rounded+1c:wght@500;700;800;900&display=swap">
<style>
  :root {
    --bg: #fdf1b4;
    --panel: #fff8d6;
    --ink: #1b1b1b;
    --orange: #f6a300;
    --orange-deep: #ee8a00;
    --text-orange: #f08a00;
    --fruit: #ffd23c;
    --fruit-edge: #f6b400;
    --white: #ffffff;
  }
  * { box-sizing: border-box; margin: 0; padding: 0; }
  html, body { width: 849px; height: 1200px; overflow: hidden; }
  body {
    background: var(--bg);
    font-family: "M PLUS Rounded 1c", sans-serif;
    color: var(--ink);
  }
  .poster {
    position: relative;
    width: 849px; height: 1200px;
    background: var(--bg);
  }
  .poster-inner {
    position: absolute; left: 22px; top: 22px; right: 22px; bottom: 22px;
    background: var(--panel);
    border-radius: 14px;
  }
  .headline {
    position: absolute; left: 48px; top: 52px; width: 740px; height: 200px;
    background: var(--ink);
    border-radius: 30px;
    color: var(--white);
    font-weight: 900;
    font-size: 66px;
    line-height: 86px;
    text-align: center;
    padding-top: 14px;
    padding-right: 40px;
    letter-spacing: 1px;
  }
  .headline-pointer { position: absolute; left: 230px; top: 240px; }
  .free-badge {
    position: absolute; left: 648px; top: 210px;
    width: 180px; height: 180px; border-radius: 50%;
    background: var(--orange);
    color: var(--white);
    font-weight: 800; text-align: center;
    display: flex; flex-direction: column; justify-content: center;
    font-size: 30px; line-height: 36px;
  }
  .free-badge .free { font-size: 44px; line-height: 52px; font-weight: 900; }
  .juice-photo {
    position: absolute; left: 52px; top: 268px; width: 320px; height: 360px;
    border-radius: 24px 24px 60px 60px;
    background: linear-gradient(180deg, #ffb21c 0%, #ffc94a 40%, #fff2d8 75%, #fbe6bf 100%);
  }
  .card-photo {
    position: absolute; left: 392px; top: 420px; width: 420px; height: 150px;
    border-radius: 10px;
    background: linear-gradient(90deg, #2a2a2a 0%, #3a3a3a 48%, #f4f1e8 52%, #ffffff 100%);
  }
  .perk {
    position: absolute; border-radius: 50%;
    background: var(--fruit);
    border: 5px solid var(--fruit-edge);
    display: flex; flex-direction: column; justify-content: center; align-items: center;
    text-align: center; font-weight: 800; color: var(--ink);
  }
  .perk-points { left: 40px; top: 660px; width: 200px; height: 200px; font-size: 24px; line-height: 34px; }
  .perk-points .big { font-size: 40px; line-height: 48px; font-weight: 900; }
  .perk-reward { left: 284px; top: 612px; width: 280px; height: 280px; font-size: 27px; line-height: 35px; }
  .perk-reward .big { font-size: 34px; font-weight: 900; color: var(--orange-deep); }
  .perk-reward .small { font-size: 16px; line-height: 24px; font-weight: 700; }
  .perk-expiry { left: 608px; top: 660px; width: 200px; height: 200px; font-size: 25px; line-height: 36px; }
  .closing {
    position: absolute; left: 0; right: 0; top: 920px;
    text-align: center; color: var(--text-orange);
    font-weight: 900; font-size: 46px; line-height: 60px;
    letter-spacing: 1px;
  }
  .footer-bar {
    position: absolute; left: 150px; right: 150px; top: 1105px; height: 72px;
    background: var(--ink);
    display: flex; align-items: center; justify-content: center; gap: 14px;
    color: var(--white); font-weight: 800; font-size: 30px; letter-spacing: 3px;
  }
  .footer-bar i { width: 30px; height: 30px; border-radius: 50%; background: var(--orange); display: block; }
</style>
</head>
<body>
<main class="poster">
  <div class="poster-inner"></div>

  <h1 class="headline">ポイントをためて<br>ジュースをゲット♪</h1>
  <svg class="headline-pointer" width="70" height="60" viewBox="0 0 70 60" aria-hidden="true">
    <polygon points="0,0 70,0 20,60" fill="var(--orange)"/>
  </svg>

  <div class="free-badge">
    <span>入会費</span><span>年会費</span><span class="free">無料</span>
  </div>

  <div class="juice-photo" role="img" aria-label="マンゴーとヨーグルトのジュースのカップ写真"></div>

  <div class="card-photo" role="img" aria-label="黒い会員カードと10マスのスタンプカードの写真"></div>

  <div class="perk perk-points">
    <span>ジュース1杯で</span><span class="big">1P</span>
  </div>
  <div class="perk perk-reward">
    <span class="big">10P</span><span>で</span><span>お好きなドリンク</span><span>1杯サービス</span>
    <span class="small">(どのサイズでもOK!)</span>
  </div>
  <div class="perk perk-expiry">
    <span>有効期限は</span><span>ありません♪</span>
  </div>

  <p class="closing">お得なポイントカード♪<br>ぜひこの機会にご入会下さい！！</p>

  <div class="footer-bar"><i></i>SUNNY PULP</div>
</main>
</body>
</html>
```